Valbrook Data Works

Our company is about IT hardwares and IT solutions. IT hardware such as PC, RAMS, storage and servers. IT solutions such as project management, BA. We are also selling new technology too.

Target Market(s)

Consumer, Small to Medium Business, Corporate

Requirements
Must have
• The business card must have the following:
• Name:
• Title:
• Contact Number:
• Email address:
• Website:
• Color: Must match the logo color upgrade

```html
<!DOCTYPE html>
<html lang="en">
<head>
<meta charset="utf-8">
<title>Valbrook Data Works – Business Card</title>
<link rel="stylesheet" href="https://fonts.googleapis.com/css2?family=Arimo:wght@400;700&display=swap">
<style>
  :root {
    --backdrop: #1f1f1f;
    --amber: #e19a3c;
    --amber-deep: #d38a2c;
    --charcoal: #3a3a3b;
    --charcoal-edge: #333334;
    --ink-dark: #404040;
    --ink-light: #e6e6e6;
    --ink-muted: #d0d0d0;
  }
  * { box-sizing: border-box; margin: 0; padding: 0; }
  html, body {
    width: 1200px;
    height: 997px;
    overflow: hidden;
    background: var(--backdrop);
    font-family: "Arimo", Arial, sans-serif;
  }
  .canvas {
    position: relative;
    width: 1200px;
    height: 997px;
  }
  .card {
    position: absolute;
    width: 560px;
    height: 320px;
    border-radius: 16px;
    box-shadow: 0 18px 40px rgba(0, 0, 0, 0.55);
  }
  .card-front {
    left: 70px;
    top: 110px;
    background: linear-gradient(160deg, var(--amber), var(--amber-deep));
    display: flex;
    align-items: center;
    justify-content: center;
  }
  .card-back {
    left: 570px;
    top: 520px;
    background: linear-gradient(160deg, var(--charcoal), var(--charcoal-edge));
  }
  .brand-name {
    font-weight: 700;
    font-size: 44px;
    line-height: 1.05;
    letter-spacing: 1px;
    text-transform: uppercase;
    text-align: center;
  }
  .card-front .brand-name { color: var(--ink-dark); }
  .card-back .brand-name {
    position: absolute;
    left: 40px;
    top: 40px;
    font-size: 40px;
    text-align: left;
    color: var(--ink-light);
  }
  .person {
    position: absolute;
    left: 40px;
    bottom: 50px;
  }
  .person-name {
    font-weight: 700;
    font-size: 20px;
    color: var(--amber);
    text-transform: uppercase;
    letter-spacing: 0.5px;
  }
  .person-title {
    font-size: 15px;
    color: var(--ink-muted);
    margin-top: 4px;
    padding-left: 60px;
  }
  .divider {
    position: absolute;
    left: 300px;
    top: 170px;
    width: 2px;
    height: 110px;
    background: linear-gradient(to bottom, transparent, var(--amber), transparent);
  }
  .contact {
    position: absolute;
    left: 330px;
    top: 175px;
    list-style: none;
    font-size: 15px;
    color: var(--ink-muted);
  }
  .contact li {
    display: flex;
    align-items: center;
    gap: 8px;
    margin-bottom: 8px;
  }
  .contact svg { width: 13px; height: 13px; fill: var(--amber); flex: none; }
  .contact .website {
    color: var(--amber);
    font-weight: 700;
    letter-spacing: 2px;
    padding-left: 21px;
  }
</style>
</head>
<body>
<main class="canvas">
  <section class="card card-front" aria-label="Card front">
    <p class="brand-name">Valbrook<br>Data Works</p>
  </section>

  <section class="card card-back" aria-label="Card back">
    <p class="brand-name">Valbrook<br>Data Works</p>
    <div class="person">
      <p class="person-name">Marcus Ellery</p>
      <p class="person-title">Director</p>
    </div>
    <div class="divider"></div>
    <ul class="contact">
      <li>
        <svg viewBox="0 0 16 16" aria-hidden="true"><path d="M3.6 1.2l2.3 2.8-1.4 1.9c.9 2 2.6 3.7 4.6 4.6l1.9-1.4 2.8 2.3-1.5 2.6C7 13.6 2.4 9 1 3.7z"/></svg>
        <span>1441 555 0142</span>
      </li>
      <li>
        <svg viewBox="0 0 16 16" aria-hidden="true"><path d="M1 3h14v1.2L8 9 1 4.2z"/><path d="M1 5.6l7 4.8 7-4.8V13H1z"/></svg>
        <span>mellery@valbrookdata.com</span>
      </li>
      <li class="website">www.valbrookdata.com</li>
    </ul>
  </section>
</main>
</body>
</html>
```